Roofing company needs a door hanger designed.

Hello, I would like to have a door hanger designed for our roofing company in Orlando Florida. I have included information about us below and attached our logo. Please let me know if there is anything else you need? thank you.

BRIGHT HARBOR ROOFING
5417 Copper Meadow Blvd. Winter Park, FL 32795
Website: brightharborroofco.example
Email: info@brightharborroofco.example
Office phone #: 407.555.0146

Notes: In the state of Florida a roofing contractor must include their license number on all documentation and marketing materials. Lic#CCC1590827

Items I would like to add:
-CALL TODAY FOR A FREE ESTIMATE
-SCHEDULE YOUR FREE INSPECTION TODAY
-OUR SERVICES: ROOF REPLACEMENT, ROOF REPAIR, EMERGENCY SERVICES
-LICENSED & INSURED
OTHER SENTENCES / PARAGRAPHS IF NEEDED.
-We at Bright Harbor Roofing are dedicated to providing superior service.
-Driven to offer the highest quality and professional commercial and residential roofing solutions at a fair price.
-Our goal is to provide you with the best value possible!
-The best option not the highest priced option. Sometimes a small roof repair is all it takes to fix your roofing issues.
-Free roof inspections and proposals that are customized to your project to solve your roofing needs.

```html
<!DOCTYPE html>
<html lang="en">
<head>
<meta charset="UTF-8">
<title>Bright Harbor Roofing – Door Hanger</title>
<link href="https://fonts.googleapis.com/css2?family=Archivo+Black&family=Noto+Sans+Mono:wght@400;700&display=swap" rel="stylesheet">
<style>
  :root {
    --page-bg: #ece9e4;
    --hanger-red: #b70c10;
    --hanger-red-light: #d4544f;
    --hanger-red-deep: #a8080b;
    --ink-white: #ffffff;
    --ink-rim: #3b2626;
    --ink-number: #2b2626;
    --icon-red: #c3161b;
    --hole: #4a2a1e;
  }
  html, body {
    margin: 0;
    padding: 0;
    width: 892px;
    height: 1200px;
    overflow: hidden;
    background: var(--page-bg);
  }
  .door-hanger {
    display: block;
    width: 892px;
    height: 1200px;
  }
  .brand-name {
    font-family: "Noto Sans Mono", monospace;
    font-weight: 700;
    fill: var(--ink-white);
  }
  .service-line {
    font-family: "Noto Sans Mono", monospace;
    font-weight: 700;
    font-size: 55px;
    fill: var(--ink-white);
  }
  .phone-number {
    font-family: "Archivo Black", "Arial Black", sans-serif;
    font-size: 54px;
    fill: var(--ink-number);
  }
  .call-to-action {
    font-family: "Noto Sans Mono", monospace;
    font-weight: 700;
    font-size: 23.5px;
    fill: var(--ink-white);
  }
  .license {
    font-family: "Noto Sans Mono", monospace;
    font-size: 9px;
    fill: var(--ink-number);
  }
  .rim-text {
    font-family: "Noto Sans Mono", monospace;
    font-weight: 400;
    fill: var(--ink-rim);
  }
  .rim-address, .rim-email { font-size: 18.5px; }
  .rim-website { font-size: 28px; }
</style>
</head>
<body>
<svg class="door-hanger" viewBox="0 0 892 1200" xmlns="http://www.w3.org/2000/svg" aria-label="Bright Harbor Roofing door hanger">
  <defs>
    <radialGradient id="hangerFill" cx="78%" cy="30%" r="85%">
      <stop offset="0" stop-color="var(--hanger-red-light)"/>
      <stop offset="0.45" stop-color="var(--hanger-red)"/>
      <stop offset="1" stop-color="var(--hanger-red-deep)"/>
    </radialGradient>
    <path id="arcAddress" d="M632,277.8 A372,372 0 0 1 750.7,813.4"/>
    <path id="arcEmail" d="M141.3,813.4 A372,372 0 0 1 232.6,295.3"/>
    <path id="arcWebsite" d="M149.5,807.6 A364,364 0 0 0 742.5,807.6"/>
  </defs>

  <!-- hanger disc -->
  <circle class="hanger-disc" cx="446" cy="600" r="410" fill="url(#hangerFill)"/>
  <circle class="hanger-hole" cx="286" cy="290" r="6" fill="var(--hole)"/>
  <circle class="hanger-hole" cx="586" cy="290" r="6" fill="var(--hole)"/>

  <!-- brand -->
  <g class="brand">
    <circle cx="446" cy="330" r="30" fill="var(--ink-white)"/>
    <text class="brand-name" x="446" y="412" font-size="44" text-anchor="middle">BRIGHT HARBOR</text>
    <text class="brand-name" x="446" y="452" font-size="30" text-anchor="middle" letter-spacing="10">ROOFING</text>
  </g>

  <!-- services -->
  <g class="services">
    <text class="service-line" x="446" y="550" text-anchor="middle">ROOF REPLACEMENT</text>
    <text class="service-line" x="446" y="603" text-anchor="middle">ROOF REPAIR</text>
    <text class="service-line" x="446" y="657" text-anchor="middle">EMERGENCY SERVICES</text>
  </g>

  <!-- phone box -->
  <g class="phone-box">
    <rect x="215" y="734" width="431" height="59" fill="var(--ink-white)"/>
    <path class="phone-icon" fill="var(--icon-red)"
          d="M222,756 c2,-4 5,-5 8,-4 l4,8 c1,2 0,3 -2,4 l-3,2 c2,5 5,9 10,12 l2,-3 c1,-2 3,-2 4,-1 l8,4 c1,3 -1,6 -4,8 c-4,2 -8,2 -12,-1 c-8,-5 -14,-12 -16,-20 c-1,-3 0,-6 1,-9 z"/>
    <path fill="none" stroke="var(--icon-red)" stroke-width="2.6" stroke-linecap="round"
          d="M242,755 a7,7 0 0 1 6,6 M243,748 a13,13 0 0 1 12,12 M244,741 a19,19 0 0 1 17,17"/>
    <text class="phone-number" x="278" y="784" textLength="352" lengthAdjust="spacingAndGlyphs">407.555.0146</text>
  </g>
  <text class="call-to-action" x="430" y="821" text-anchor="middle">CALL TODAY FOR A FREE ESTIMATE</text>

  <text class="license" x="430" y="903" text-anchor="middle">LIC#CCC1590827</text>

  <!-- rim text -->
  <text class="rim-text rim-address"><textPath href="#arcAddress" startOffset="50%" text-anchor="middle">5417 Copper Meadow Blvd. Winter Park, FL 32795</textPath></text>
  <text class="rim-text rim-email"><textPath href="#arcEmail" startOffset="50%" text-anchor="middle">Email: info@brightharborroofco.example</textPath></text>
  <text class="rim-text rim-website"><textPath href="#arcWebsite" startOffset="50%" text-anchor="middle">www.brightharborroofco.example</textPath></text>
</svg>
</body>
</html>
```